Medically supervised Weight loss program

I would like to keep a similar layout to the existing business card, maybe adjust the logo a bit. Perhaps new ideas other than the scale. The ORB which is The parent company should be incorporated into the logo and may be subtle. The logo will also be used on the company website. The colors should represent health and wellness.

Target Market(s)

Overweight age 18 and up

Industry/Entity Type

Medical

Contact Information for Business Card

Same layout preferred

Font styles to use
Other font styles liked:
• Same as attached card

Requirements
Must have
• The circular Logo ORB needs to be incorporated somehow
Nice to have
• Logo should represent a weight loss program and incorporate the ORB

```html
<!DOCTYPE html>
<html lang="en">
<head>
<meta charset="utf-8">
<title>ORB Weight Management – Business Card</title>
<link rel="stylesheet" href="https://fonts.googleapis.com/css2?family=Arimo:wght@700&family=Libre+Baskerville:ital,wght@0,400;0,700;1,400;1,700&display=swap">
<style>
  :root {
    --brand-blue: #079ec4;
    --accent-yellow: #fff200;
    --ink: #111111;
    --paper: #ffffff;
    --backdrop: #e9ecee;
    --card-w: 680px;
    --card-h: 388px;
  }
  * { box-sizing: border-box; margin: 0; padding: 0; }
  html, body { width: 1200px; height: 900px; overflow: hidden; }
  body {
    background: var(--backdrop);
    position: relative;
    font-family: "Arimo", Arial, sans-serif;
  }
  .card {
    position: absolute;
    left: 260px;
    width: var(--card-w);
    height: var(--card-h);
    overflow: hidden;
    box-shadow: 0 6px 18px rgba(0,0,0,.18);
  }
  .card--back { top: 40px; background: var(--brand-blue); }
  .card--front { top: 472px; background: var(--paper); }

  .brand-mark {
    position: absolute;
    display: flex;
    align-items: center;
    gap: 14px;
    color: var(--paper);
    font-family: "Arimo", Arial, sans-serif;
    font-weight: 700;
    text-transform: uppercase;
    line-height: 1.1;
  }
  .brand-mark__dot {
    flex: none;
    border-radius: 50%;
    background: var(--accent-yellow);
  }
  .card--back .brand-mark {
    left: 50%; top: 50%;
    transform: translate(-50%, -50%);
    font-size: 34px;
  }
  .card--back .brand-mark__dot { width: 56px; height: 56px; }

  .front-shapes { position: absolute; inset: 0; }

  .front-brand { left: 34px; top: 40px; font-size: 24px; }
  .front-brand .brand-mark__dot { width: 40px; height: 40px; }

  .contact {
    position: absolute;
    left: 34px;
    top: 180px;
    color: var(--paper);
    font-size: 19px;
    line-height: 1.3;
  }
  .contact__phones { margin-top: 14px; }

  .practice {
    position: absolute;
    left: 390px;
    top: 40px;
    width: 270px;
    color: var(--ink);
    font-family: "Libre Baskerville", "Times New Roman", serif;
  }
  .practice__name {
    font-size: 25px;
    font-weight: 700;
    line-height: 1.05;
    text-transform: uppercase;
  }
  .practice__tagline {
    font-size: 13px;
    font-style: italic;
    font-weight: 700;
    margin-top: 4px;
  }
  .clinician { margin-top: 18px; }
  .clinician + .clinician { margin-top: 12px; }
  .clinician__name {
    color: var(--brand-blue);
    font-size: 19px;
    font-weight: 700;
  }
  .clinician__name--caps { text-transform: uppercase; }
  .clinician__role {
    font-size: 13px;
    font-style: italic;
    line-height: 1.3;
  }
  .practice__note {
    margin-top: 34px;
    text-align: right;
    font-size: 15px;
    font-style: italic;
  }
</style>
</head>
<body>

  <section class="card card--back" aria-label="Business card back">
    <div class="brand-mark">
      <span class="brand-mark__dot"></span>
      <span>ORB Weight<br>Management</span>
    </div>
  </section>

  <section class="card card--front" aria-label="Business card front">
    <svg class="front-shapes" width="680" height="388" viewBox="0 0 680 388" aria-hidden="true">
      <polygon points="0,0 384,0 304,388 0,388" fill="#079ec4"/>
      <polygon points="384,0 398,0 318,388 304,388" fill="#fff200"/>
    </svg>

    <div class="brand-mark front-brand">
      <span class="brand-mark__dot"></span>
      <span>ORB Weight<br>Management</span>
    </div>

    <address class="contact" style="font-style:normal">
      <div>1480 MEADOW RIDGE RD.</div>
      <div>SUITE 210</div>
      <div>LAKEVIEW, NY 11590</div>
      <div class="contact__phones">
        <div>Tel 516-555-0142</div>
        <div>Fax 516-555-0187</div>
      </div>
    </address>

    <div class="practice">
      <h1 class="practice__name">ORB Weight Management</h1>
      <p class="practice__tagline">Personalized &amp; Medically Supervised</p>

      <div class="clinician">
        <p class="clinician__name clinician__name--caps">Dr. Daniel Hartwell</p>
        <p class="clinician__role">Diplomate, American Board<br>of Internal Medicine</p>
      </div>
      <div class="clinician">
        <p class="clinician__name">Marla Kessing, NP-BC</p>
        <p class="clinician__role">Board Certified Nurse Practitioner</p>
      </div>

      <p class="practice__note">By Appointment Only</p>
    </div>
  </section>

</body>
</html>
```